KVRo Business Cards

We need a business card design. We are a Technology (Audio Visual) design, sales and installation company. Looking for a double sided design, clean

Contact Information for Business Card

Clean, modern look, 2 sided

Font styles to use
Sans Serif

```html
<!DOCTYPE html>
<html lang="en">
<head>
<meta charset="utf-8">
<title>KVRo Business Card</title>
<link rel="stylesheet" href="https://fonts.googleapis.com/css2?family=Montserrat:wght@500;700;800&display=swap">
<style>
  :root {
    --ink: #1f2d3d;
    --accent: #f7941d;
    --paper: #ffffff;
    --page: #eef1f5;
    --deep-blue: #0a1a8c;
    --mid-blue: #1f4fe0;
    --cyan: #22d3f5;
    --violet: #5a1fc9;
  }
  * { margin: 0; padding: 0; box-sizing: border-box; }
  html, body {
    width: 1200px;
    height: 686px;
    overflow: hidden;
    background: var(--page);
  }
  .card {
    position: relative;
    width: 1200px;
    height: 686px;
    border-radius: 24px;
    overflow: hidden;
    background: var(--paper);
    font-family: "Montserrat", Arial, sans-serif;
    color: var(--ink);
  }
  .hero-art {
    position: absolute;
    left: 0; top: 0;
    width: 1200px;
    height: 434px;
    background:
      radial-gradient(ellipse 520px 260px at 60% 92%, rgba(120, 240, 255, 0.85), rgba(34, 211, 245, 0) 70%),
      radial-gradient(ellipse 400px 300px at 88% 40%, rgba(34, 211, 245, 0.55), rgba(34, 211, 245, 0) 70%),
      radial-gradient(ellipse 380px 260px at 10% 30%, rgba(90, 31, 201, 0.6), rgba(90, 31, 201, 0) 70%),
      linear-gradient(180deg, var(--deep-blue) 0%, var(--mid-blue) 55%, var(--cyan) 100%);
  }
  .footer-art {
    position: absolute;
    left: 0; bottom: 0;
    width: 1200px;
    height: 40px;
    background: linear-gradient(90deg, var(--deep-blue) 0%, var(--mid-blue) 40%, var(--cyan) 60%, var(--mid-blue) 100%);
  }
  .logo-tab {
    position: absolute;
    left: 394px; top: 0;
    width: 413px;
    height: 295px;
    background: var(--paper);
    border-radius: 0 0 34px 34px;
    display: flex;
    align-items: center;
    justify-content: center;
    padding-top: 8px;
  }
  .brand-name {
    font-weight: 800;
    font-size: 112px;
    letter-spacing: -2px;
    color: var(--ink);
    line-height: 1;
  }
  .contacts {
    position: absolute;
    left: 0; top: 434px;
    width: 1200px;
    height: 212px;
  }
  .contact {
    position: absolute;
    height: 44px;
    font-weight: 500;
    font-size: 35px;
    line-height: 44px;
    color: var(--ink);
    white-space: nowrap;
  }
  .contact svg {
    position: absolute;
    left: 0; top: 3px;
    width: 38px;
    height: 38px;
    fill: var(--accent);
  }
  .contact .label {
    position: absolute;
    left: 75px; top: 0;
  }
  .contact--phone   { left: 30px;  top: 47px; }
  .contact--address { left: 30px;  top: 115px; }
  .contact--email   { left: 640px; top: 47px; }
  .contact--web     { left: 640px; top: 115px; }
  .contact--email .label,
  .contact--web .label { left: 85px; }
</style>
</head>
<body>
  <div class="card">
    <div class="hero-art" role="img" aria-label="Neon blue and cyan candlestick market chart over a dotted world map"></div>

    <div class="logo-tab">
      <span class="brand-name">KVRo</span>
    </div>

    <div class="contacts">
      <div class="contact contact--phone">
        <svg viewBox="0 0 24 24" aria-hidden="true"><path d="M6.6 10.8a15.1 15.1 0 0 0 6.6 6.6l2.2-2.2a1 1 0 0 1 1-.25 11.4 11.4 0 0 0 3.6.57 1 1 0 0 1 1 1V20a1 1 0 0 1-1 1A17 17 0 0 1 3 4a1 1 0 0 1 1-1h3.5a1 1 0 0 1 1 1c0 1.25.2 2.45.57 3.57a1 1 0 0 1-.25 1z"/></svg>
        <span class="label">555 214 8830</span>
      </div>
      <div class="contact contact--address">
        <svg viewBox="0 0 24 24" aria-hidden="true"><path d="M12 2a7 7 0 0 0-7 7c0 5.2 7 13 7 13s7-7.8 7-13a7 7 0 0 0-7-7zm0 9.6A2.6 2.6 0 1 1 12 6.4a2.6 2.6 0 0 1 0 5.2z"/></svg>
        <span class="label">48 Oak Lane, Northfield</span>
      </div>
      <div class="contact contact--email">
        <svg viewBox="0 0 24 24" aria-hidden="true"><path d="M2 5h20v2.2l-10 6.3L2 7.2z"/><path d="M2 9.4l10 6.3 10-6.3V19H2z"/></svg>
        <span class="label">hello@kvro-av.com</span>
      </div>
      <div class="contact contact--web">
        <svg viewBox="0 0 24 24" aria-hidden="true"><path d="M12 2a10 10 0 1 0 0 20 10 10 0 0 0 0-20zm6.9 6h-2.9a15.6 15.6 0 0 0-1.4-3.6A8 8 0 0 1 18.9 8zM12 4c.8 1.2 1.5 2.5 1.9 4h-3.8c.4-1.5 1.1-2.8 1.9-4zM4.3 14a8.2 8.2 0 0 1 0-4h3.4a16.5 16.5 0 0 0 0 4zm.8 2h2.9c.3 1.3.8 2.5 1.4 3.6A8 8 0 0 1 5.1 16zM8 8H5.1a8 8 0 0 1 4.3-3.6C8.8 5.5 8.3 6.7 8 8zm4 12c-.8-1.2-1.5-2.5-1.9-4h3.8c-.4 1.5-1.1 2.8-1.9 4zm2.3-6H9.7a14.7 14.7 0 0 1 0-4h4.6a14.7 14.7 0 0 1 0 4zm.3 5.6c.6-1.1 1.1-2.3 1.4-3.6h2.9a8 8 0 0 1-4.3 3.6zm1.7-5.6a16.5 16.5 0 0 0 0-4h3.4a8.2 8.2 0 0 1 0 4z"/></svg>
        <span class="label">www.kvroavsite.com</span>
      </div>
    </div>

    <div class="footer-art" role="img" aria-label="Strip of the blue market chart artwork"></div>
  </div>
</body>
</html>
```